Dog care service needs business card design

Our company is Pawsome Haven. We provide care for dogs while their owners are away, either through home visits or a holiday stay in the homes of carefully selected minders. Our existing website & Chatterbook cover should provide all the colour cues for our business cards - namely blues, blondes and grey. We have an existing logo (provided).

www.pawsomehaven-demo.com.au
www.facebook.com/pawsomehavenau

We wish to clearly communicate our three areas of service "dog minding, home visits, dog walking".

We would like to have the files ready for upload to Prontoprint (or similar) for immediate printing.

Target Market(s)

Dog owners who love their dogs like family

Industry/Entity Type

Business

Contact Information for Business Card

Pawsome Haven
Ph: 0491 574 318

Font styles to use
Sans Serif

Colors
33a6d7
3176b5

Requirements
Must have
• Logo
• Telephone number
• website
• "Dog minding, home visits, dog walking"
Should not have
• any additional illustrations beyond the logo.

```html
<!DOCTYPE html>
<html lang="en">
<head>
<meta charset="utf-8">
<title>Pawsome Haven – Business Card</title>
<link rel="stylesheet" href="https://fonts.googleapis.com/css2?family=Lexend:wght@500;600&family=Questrial&display=swap">
<style>
  :root {
    --backdrop: #ececee;
    --card: #ffffff;
    --slate: #3b4656;
    --blue: #2f9ad8;
    --blue-soft: #dcebf5;
    --slate-soft: #c9ced6;
  }
  * { box-sizing: border-box; margin: 0; padding: 0; }
  html, body {
    width: 1200px;
    height: 600px;
    overflow: hidden;
    background: var(--backdrop);
  }
  .canvas {
    position: relative;
    width: 1200px;
    height: 600px;
  }
  .card {
    position: absolute;
    top: 152px;
    width: 467px;
    height: 278px;
    background: var(--card);
    border-radius: 16px;
    overflow: hidden;
    box-shadow: 0 6px 18px rgba(40, 50, 70, 0.12);
  }
  .card--front { left: 93px; }
  .card--back { left: 638px; }

  /* Front lockup */
  .lockup {
    position: absolute;
    left: 70px;
    top: 96px;
    display: flex;
    align-items: center;
    gap: 18px;
  }
  .lockup__mark {
    width: 62px;
    height: 62px;
    border-radius: 50%;
    background: var(--slate);
    flex: none;
  }
  .wordmark {
    font-family: "Lexend", sans-serif;
    font-weight: 600;
    color: var(--slate);
    line-height: 0.98;
    letter-spacing: -0.5px;
  }
  .lockup .wordmark { font-size: 34px; }
  .tagline {
    font-family: "Questrial", sans-serif;
    color: var(--blue);
    text-transform: uppercase;
    letter-spacing: 4px;
  }
  .lockup .tagline {
    font-size: 11px;
    margin-top: 7px;
    padding-left: 4px;
  }

  /* Back side */
  .back-brand {
    position: absolute;
    left: 27px;
    top: 44px;
  }
  .back-brand .wordmark { font-size: 25px; }
  .back-brand .tagline {
    font-size: 8.5px;
    letter-spacing: 3px;
    margin-top: 5px;
    padding-left: 26px;
  }
  .contact {
    position: absolute;
    left: 27px;
    top: 126px;
    font-family: "Questrial", sans-serif;
    font-size: 12px;
    line-height: 17px;
    color: var(--slate);
  }
  .contact strong { font-weight: 700; }
  .services {
    position: absolute;
    left: 27px;
    top: 183px;
    list-style: none;
    font-family: "Questrial", sans-serif;
    font-size: 12px;
    line-height: 17px;
    color: var(--blue);
  }
  .services li {
    display: flex;
    align-items: center;
    gap: 5px;
  }
  .paw { width: 10px; height: 10px; flex: none; }
  .paw circle, .paw ellipse { fill: var(--slate); }

  .mascot-area {
    position: absolute;
    left: 222px;
    top: 60px;
    width: 245px;
    height: 218px;
    border-top-left-radius: 110px;
    background: linear-gradient(135deg, var(--slate-soft) 0%, var(--blue-soft) 100%);
  }
</style>
</head>
<body>
<main class="canvas">

  <section class="card card--front" aria-label="Card front">
    <div class="lockup">
      <span class="lockup__mark" aria-hidden="true"></span>
      <div>
        <div class="wordmark">Pawsome<br>Haven</div>
        <div class="tagline">Pet Services</div>
      </div>
    </div>
  </section>

  <section class="card card--back" aria-label="Card back">
    <div class="back-brand">
      <div class="wordmark">Pawsome<br>Haven</div>
      <div class="tagline">Pet Services</div>
    </div>

    <p class="contact">
      Phone: 0491 574 318<br>
      www.<strong>pawsomehaven-demo</strong>.com.au
    </p>

    <ul class="services">
      <li>
        <svg class="paw" viewBox="0 0 10 10" aria-hidden="true"><ellipse cx="5" cy="7" rx="2.6" ry="2.2"/><circle cx="1.5" cy="4.2" r="1.1"/><circle cx="3.6" cy="2" r="1.1"/><circle cx="6.4" cy="2" r="1.1"/><circle cx="8.5" cy="4.2" r="1.1"/></svg>
        dog minding
      </li>
      <li>
        <svg class="paw" viewBox="0 0 10 10" aria-hidden="true"><ellipse cx="5" cy="7" rx="2.6" ry="2.2"/><circle cx="1.5" cy="4.2" r="1.1"/><circle cx="3.6" cy="2" r="1.1"/><circle cx="6.4" cy="2" r="1.1"/><circle cx="8.5" cy="4.2" r="1.1"/></svg>
        home visitng
      </li>
      <li>
        <svg class="paw" viewBox="0 0 10 10" aria-hidden="true"><ellipse cx="5" cy="7" rx="2.6" ry="2.2"/><circle cx="1.5" cy="4.2" r="1.1"/><circle cx="3.6" cy="2" r="1.1"/><circle cx="6.4" cy="2" r="1.1"/><circle cx="8.5" cy="4.2" r="1.1"/></svg>
        dog walking
      </li>
    </ul>

    <div class="mascot-area" role="img" aria-label="Large cropped brand mascot illustration bleeding off the right edge"></div>
  </section>

</main>
</body>
</html>
```